Tidewell Outfitters Mobile RV Repair

We are looking for a logo and business cards for a new start up business. We will be doing Mobile RV Repair.
We are in Texas.
I don't have any designs at this point.

Contact Information for Business Card

Emphasis should be on the “Mobile RV Repair” and not so much the name “Tidewell Outfitters”

Requirements
Nice to have
• I like the Mobile RV Repair to cover most of the backside of the card! Not sure on the colors, would like to see it in a few different colors!

```html
<!DOCTYPE html>
<html lang="en">
<head>
<meta charset="utf-8">
<title>Tidewell Outfitters Mobile RV Repair – Business Card</title>
<link rel="stylesheet" href="https://fonts.googleapis.com/css2?family=Jura:wght@300;500;600&family=Lexend:wght@500&display=swap">
<style>
  :root {
    --backdrop: #504e4d;
    --card-dark: #222222;
    --band-dark: #353535;
    --orange: #e8701f;
    --orange-deep: #b8561a;
    --paper-light: #f7f7f7;
    --paper-shade: #d6d6d6;
    --ink: #222222;
    --text-light: #eeeeee;
  }
  html, body {
    margin: 0;
    width: 1200px;
    height: 1200px;
    overflow: hidden;
    background: var(--backdrop);
  }
  .canvas {
    position: relative;
    width: 1200px;
    height: 1200px;
  }
  .card {
    position: absolute;
    left: 243px;
    width: 702px;
    height: 400px;
    display: block;
  }
  .card--front { top: 170px; }
  .card--back { top: 630px; }
  .font-tech { font-family: "Jura", sans-serif; }
  .font-brand { font-family: "Lexend", sans-serif; }
</style>
</head>
<body>
<main class="canvas">

  <!-- Front: service headline -->
  <svg class="card card--front" viewBox="0 0 702 400" aria-label="Front of business card">
    <defs>
      <clipPath id="front-shape"><rect width="702" height="400" rx="22"/></clipPath>
    </defs>
    <g clip-path="url(#front-shape)">
      <rect class="front-base" width="702" height="400" fill="var(--card-dark)"/>
      <rect class="phone-stripe" width="67" height="400" fill="var(--orange)"/>
    </g>
    <text class="phone-vertical font-tech" transform="translate(48 374) rotate(-90)"
          font-size="44" font-weight="600" fill="var(--text-light)"
          textLength="348" lengthAdjust="spacingAndGlyphs">210-555-0148</text>
    <text class="headline-mobile font-tech" x="129" y="158" font-size="62" font-weight="300"
          fill="var(--text-light)" textLength="529" lengthAdjust="spacing">MOBILE</text>
    <text class="headline-service font-brand" x="122" y="262" font-size="120" font-weight="500"
          textLength="539" lengthAdjust="spacingAndGlyphs"><tspan fill="var(--orange)">RV</tspan><tspan fill="var(--text-light)" dx="10">Repair</tspan></text>
  </svg>

  <!-- Back: name and contact -->
  <svg class="card card--back" viewBox="0 0 702 400" aria-label="Back of business card">
    <defs>
      <clipPath id="back-shape"><rect width="702" height="400" rx="22"/></clipPath>
      <linearGradient id="paper" x1="0" y1="0" x2="1" y2="1">
        <stop offset="0" stop-color="var(--paper-light)"/>
        <stop offset="1" stop-color="var(--paper-shade)"/>
      </linearGradient>
      <linearGradient id="orange-panel" x1="0" y1="0" x2="0.4" y2="1">
        <stop offset="0" stop-color="var(--orange)"/>
        <stop offset="1" stop-color="var(--orange-deep)"/>
      </linearGradient>
    </defs>
    <g clip-path="url(#back-shape)">
      <rect class="paper-panel" width="367" height="400" fill="url(#paper)"/>
      <rect class="orange-panel" x="367" width="335" height="400" fill="url(#orange-panel)"/>
      <polygon class="band-fold" points="348,118 367,118 367,137" fill="#1a1a1a"/>
      <rect class="name-band" x="348" y="39" width="354" height="79" fill="var(--band-dark)"/>
      <polygon class="band-fold" points="348,266 367,247 367,266" fill="#1a1a1a"/>
      <rect class="contact-band" x="348" y="266" width="354" height="106" fill="var(--band-dark)"/>
    </g>

    <!-- Company name lockup -->
    <circle class="brand-mark" cx="171" cy="170" r="30" fill="var(--ink)"/>
    <text class="brand-name font-brand" x="171" y="246" text-anchor="middle" font-size="25"
          font-weight="500" fill="var(--ink)" textLength="216" lengthAdjust="spacingAndGlyphs">Tidewell Outfitters</text>
    <text class="brand-tagline font-tech" x="171" y="266" text-anchor="middle" font-size="15"
          font-weight="500" fill="var(--ink)" textLength="214" lengthAdjust="spacing">MOBILE RV REPAIR</text>

    <!-- Person -->
    <text class="person-name font-tech" x="386" y="90" font-size="29" font-weight="600"
          fill="var(--text-light)">DALE HARMON</text>

    <!-- Phone -->
    <g class="contact-phone">
      <circle cx="369" cy="298" r="11" fill="#e6e6e6"/>
      <path d="M364.5 292.5c1-.8 1.9-.6 2.4.3l1 1.8c.4.8.2 1.5-.5 2l-.8.6c.6 1.6 1.7 2.8 3.3 3.5l.6-.8c.5-.7 1.2-.9 2-.5l1.8 1c.9.5 1.1 1.4.3 2.4-1.1 1.2-2.6 1.5-4.3.7-3-1.4-5.2-3.7-6.5-6.6-.7-1.7-.4-3.3.7-4.4z" fill="var(--band-dark)"/>
      <text class="font-tech" x="395" y="304" font-size="17" font-weight="500" fill="#e6e6e6" letter-spacing="0.5">210-555-0148</text>
    </g>

    <!-- Email -->
    <g class="contact-email">
      <circle cx="369" cy="340" r="11" fill="#e6e6e6"/>
      <rect x="362.5" y="335.5" width="13" height="9" rx="1.5" fill="none" stroke="var(--band-dark)" stroke-width="1.6"/>
      <polyline points="363,336.5 369,341 375,336.5" fill="none" stroke="var(--band-dark)" stroke-width="1.6"/>
      <text class="font-tech" x="395" y="346" font-size="17" font-weight="500" fill="#e6e6e6" letter-spacing="0.5">TidewellRV@mailbox.com</text>
    </g>
  </svg>

</main>
</body>
</html>
```